Ledgerwise Business Card Design

Business Card Design for new business called Ledgerwise focused on selling business software to small and medium size companies who have outgrown Tallymark. Similar companies would be Tallymark, Nuvo, CoreFlow. Also Dealharbor would be good to look at for additional ideas around look and feel.

Target Market(s)

Business to Business

Industry/Entity Type

Information Technology

Contact Information for Business Card

Standard Business Card Information

Font styles to use
Sans Serif

```html
<!DOCTYPE html>
<html lang="en">
<head>
<meta charset="utf-8">
<title>Ledgerwise Business Card</title>
<link href="https://fonts.googleapis.com/css2?family=Roboto:wght@400;500;700&family=Saira+Semi+Condensed:wght@600&display=swap" rel="stylesheet">
<style>
  :root {
    --navy: #0b4877;
    --orange: #ee7d0d;
    --paper: #f3f4f6;
    --backdrop: #e7e6e3;
    --white: #ffffff;
  }
  html, body {
    margin: 0;
    padding: 0;
    width: 1193px;
    height: 1200px;
    overflow: hidden;
    background: var(--backdrop);
    font-family: "Roboto", Arial, sans-serif;
  }
  .canvas { position: relative; width: 1193px; height: 1200px; }
  .card { position: absolute; left: 212px; width: 720px; height: 427px; box-shadow: 0 2px 6px rgba(0,0,0,0.12); }
  .card-front { top: 158px; background: var(--navy); }
  .card-back { top: 642px; background: var(--paper); }

  .wordmark {
    position: absolute;
    display: flex;
    align-items: center;
    gap: 14px;
    font-family: "Roboto", Arial, sans-serif;
    font-weight: 700;
    letter-spacing: -1px;
    white-space: nowrap;
  }
  .wordmark-dot { border-radius: 50%; background: var(--orange); flex: none; }
  .card-front .wordmark { left: 50%; top: 50%; transform: translate(-50%, -50%); font-size: 66px; color: var(--white); }
  .card-front .wordmark-dot { width: 40px; height: 40px; }
  .card-back .wordmark { left: 48px; top: 90px; height: 44px; font-size: 44px; color: var(--navy); }
  .card-back .wordmark-dot { width: 28px; height: 28px; }

  .accent-bar { position: absolute; left: 0; top: 90px; width: 10px; height: 45px; background: var(--navy); }
  .web-band {
    position: absolute; left: 372px; right: 0; top: 89px; height: 46px;
    background: var(--orange); color: var(--white);
    font-size: 19px; line-height: 46px; padding-left: 44px; box-sizing: border-box;
  }
  .person { position: absolute; left: 48px; top: 280px; color: var(--navy); }
  .person-name { font-family: "Saira Semi Condensed", "Arial Narrow", sans-serif; font-weight: 600; font-size: 29px; line-height: 34px; margin: 0; }
  .person-title { font-size: 17px; margin: 8px 0 0; }
  .contacts { position: absolute; left: 304px; top: 282px; margin: 0; padding: 0; list-style: none; color: var(--navy); font-size: 19px; }
  .contacts li { display: flex; align-items: center; height: 29px; }
  .contacts svg { width: 18px; height: 18px; margin-right: 18px; fill: var(--orange); flex: none; }
</style>
</head>
<body>
<div class="canvas">
  <section class="card card-front">
    <div class="wordmark"><span class="wordmark-dot"></span>Ledgerwise</div>
  </section>

  <section class="card card-back">
    <div class="accent-bar"></div>
    <div class="wordmark"><span class="wordmark-dot"></span>Ledgerwise</div>
    <div class="web-band">www.yourwebsite.com</div>

    <div class="person">
      <p class="person-name">Your Long Name</p>
      <p class="person-title">Managing Director</p>
    </div>

    <ul class="contacts">
      <li>
        <svg viewBox="0 0 20 20" aria-hidden="true"><path d="M2 6c0-2 3-3 8-3s8 1 8 3v2h-4V6.5c-1-.4-2.4-.5-4-.5s-3 .1-4 .5V8H2z"/><path d="M5 9h10l2 8H3z"/></svg>
        +00 111 222 3333
      </li>
      <li>
        <svg viewBox="0 0 20 20" aria-hidden="true"><path d="M1 4h18v12H1z M3 5.5l7 5 7-5z" fill-rule="evenodd"/></svg>
        yourname@yourwebsite.com
      </li>
      <li>
        <svg viewBox="0 0 20 20" aria-hidden="true"><path fill-rule="evenodd" d="M10 1a9 9 0 1 0 0 18 9 9 0 0 0 0-18zm-1 2.2C7.7 4.5 7 6.5 6.9 9H3.1A7 7 0 0 1 9 3.2zm2 0A7 7 0 0 1 16.9 9h-3.8c-.1-2.5-.8-4.5-2.1-5.8zM9 5v4H8.9c.1-1.7.1-3 .1-4zm2 0c.6 1 1 2.4 1.1 4H11zM3.1 11h3.8c.1 2.5.8 4.5 2.1 5.8A7 7 0 0 1 3.1 11zm5.8 0H9v4c-.4-1-.1-2.3-.1-4zm2.1 0h1.1c-.1 1.6-.5 3-1.1 4zm2.1 0h3.8a7 7 0 0 1-5.9 5.8c1.3-1.3 2-3.3 2.1-5.8z"/></svg>
        Your Long Commercial address 2 line
      </li>
    </ul>
  </section>
</div>
</body>
</html>
```